Tovira Botanics Website Revamping for Ecommerce

Looking to upgrade our website and provide a better experience to users both visually and from a navigation standpoint. Here is our current site

http://toviraleafworks dot com/

Below are some Shopify Design Concepts We Like.
https://lumbergloss. com/pages/classic
https://www.korvabites. com/
https://www.quillmarrowfen. com/

Target Market(s)

People with Darker Skin Tone (Black and Brown)

Industry/Entity Type

Skin Care Product

Number of Pages Required

4 page

Requirements
Must have
• Use the Brand Guide
Nice to have
• Focus on E-Commerce Platforms such as Shopify but can be other platforms too
Should not have
• Don't deviate from Brand Guide (Attached)

```html
<!DOCTYPE html>
<html lang="en">
<head>
<meta charset="utf-8">
<title>Tovira Botanics — Rule Your Skin</title>
<link href="https://fonts.googleapis.com/css2?family=Josefin+Sans:wght@300;400;600&family=Lato:wght@400;700&family=Playfair+Display:wght@700&display=swap" rel="stylesheet">
<style>
:root{
  --green:#1f8c3b;
  --green-dark:#146b2a;
  --green-soft:#e3f0d2;
  --brown:#5b2416;
  --brown-btn:#6d2a1a;
  --grey-bg:#f2f2f2;
  --text:#333;
  --star:#f5b400;
}
*{margin:0;padding:0;box-sizing:border-box}
html,body{width:727px;height:1200px;overflow:hidden;background:#fff}
body{position:relative;font-family:"Josefin Sans",sans-serif;color:var(--text)}
.abs{position:absolute}

/* header */
.hero{left:0;top:0;width:727px;height:364px;background:radial-gradient(ellipse at 70% 40%,#ffffff 0%,#f3f8ea 45%,#d5e9b8 80%,#c3df9d 100%)}
.logo{left:80px;top:22px;font:300 25px/1 "Josefin Sans",sans-serif;color:var(--green);display:flex;align-items:center;gap:5px}
.logo .dot{width:7px;height:7px;border-radius:50%;background:var(--green)}
.nav{left:323px;top:21px;display:flex;gap:13px;font:600 6.5px/1 "Lato",sans-serif;color:#222;letter-spacing:.2px}
.nav .active{color:var(--green)}
.social{display:flex;gap:9px}
.social span{width:6px;height:6px;border-radius:50%;background:#777;display:block}
.header-social{left:542px;top:21px}
.cart{left:632px;top:17px}

.hero-photo{left:106px;top:58px;width:226px;height:306px;border-radius:110px 110px 0 0;
  background:linear-gradient(180deg,#3a2a22 0%,#5e3f30 22%,#a26f52 40%,#b98463 62%,#c79a7a 85%,#d8c0a0 100%);
  -webkit-mask-image:linear-gradient(90deg,transparent 0%,#000 14%,#000 86%,transparent 100%);
          mask-image:linear-gradient(90deg,transparent 0%,#000 14%,#000 86%,transparent 100%)}
.hero-bottles{left:318px;top:214px;width:108px;height:140px;border-radius:14px 14px 6px 6px;
  background:linear-gradient(90deg,#0d5e22 0%,#27a546 22%,#0f6a27 40%,#2aa94a 62%,#0f6a27 80%,#22983f 100%)}

.hero-title{left:437px;top:99px;font:400 27px/1 "Josefin Sans",sans-serif;color:var(--brown);letter-spacing:.3px}
.hero-sub{left:534px;top:130px;font:300 16px/1 "Josefin Sans",sans-serif;color:var(--green)}
.steps{left:438px;top:162px;list-style:none}
.steps li{display:flex;align-items:center;gap:6px;font:300 12.5px/1 "Josefin Sans",sans-serif;color:#222;height:27.5px}
.badges{left:498px;top:280px;display:flex;gap:6px}
.badge{width:46px;height:46px;border-radius:50%;border:2px solid var(--green);background:var(--green-soft);box-shadow:inset 0 0 0 4px var(--green-soft),inset 0 0 0 5px var(--green)}
.badge i{display:block;width:16px;height:16px;margin:13px auto;border-radius:50%;background:var(--green)}

/* promo tiles */
.tile{top:373px;width:277px;height:181px;display:flex;flex-direction:column;align-items:center;justify-content:center;gap:12px;color:#fff}
.tile-a{left:82px;background:linear-gradient(180deg,#a6c43a 0%,#7fa52a 55%,#c9d46a 100%)}
.tile-b{left:368px;background:linear-gradient(180deg,#e6ecb8 0%,#9fbd52 45%,#3f7e1e 100%)}
.tile h2{font:300 19px/1 "Josefin Sans",sans-serif;letter-spacing:.3px}
.btn-green{background:var(--green);color:#fff;font:700 6.5px/1 "Lato",sans-serif;padding:6px 12px;border-radius:10px}

/* products */
.section-title{left:0;width:727px;top:580px;text-align:center;font:300 13px/1 "Josefin Sans",sans-serif;color:#222}
.product{top:618px;width:140px;display:flex;flex-direction:column;align-items:center}
.product .shot{width:34px;height:134px;border-radius:8px 8px 4px 4px;background:linear-gradient(90deg,#0d5e22,#1f9c3e 50%,#0d5e22)}
.product h3{margin-top:22px;font:700 8px/1 "Lato",sans-serif;color:var(--brown)}
.product .stars{margin-top:3px;font-size:7px;color:var(--star);letter-spacing:1px}
.product .price{margin-top:5px;font:700 9px/1 "Lato",sans-serif;color:var(--green)}
.btn-outline{margin-top:8px;width:62px;height:18px;border:1px solid var(--brown-btn);border-radius:9px;font:700 6px/16px "Lato",sans-serif;text-align:center;color:#333}

/* testimonial */
.testimonial{left:0;top:860px;width:727px;height:122px;background:var(--grey-bg)}
.t-heading{left:129px;top:906px;font:400 12.5px/1.1 "Josefin Sans",sans-serif;color:#222}
.t-rule{left:254px;top:886px;width:1px;height:68px;background:#d0d0d0}
.t-photo{left:273px;top:886px;width:68px;height:68px;border-radius:50%;background:radial-gradient(circle,#8a5a44 0%,#5a3828 60%,#2a1c16 100%)}
.t-quote{left:356px;top:887px;font:700 18px/1 "Playfair Display",serif;color:var(--green)}
.t-text{left:372px;top:891px;width:274px;font:400 7px/1.65 "Lato",sans-serif;color:#555}
.t-name{left:372px;top:946px;font:700 6px/1 "Lato",sans-serif;color:var(--brown)}
.dots{left:589px;top:947px;display:flex;gap:3px}
.dots span{width:5px;height:5px;border-radius:50%;background:#ccc}
.dots .on{background:var(--green)}

/* press */
.press{left:90px;top:1010px;width:550px;display:flex;justify-content:space-between;align-items:center;color:#9a9a9a}
.press span{font:400 13px/1 "Josefin Sans",sans-serif}
.press .box{width:37px;height:36px;background:#c8c8c8}

/* newsletter */
.newsletter{left:0;top:1072px;width:727px;height:54px;background:linear-gradient(90deg,#3aa655,#2a9446 50%,#3aa655)}
.nl-icon{left:131px;top:1086px}
.nl-title{left:163px;top:1088px;font:400 11px/1 "Josefin Sans",sans-serif;color:#fff}
.nl-sub{left:165px;top:1102px;font:400 7px/1 "Lato",sans-serif;color:#eaf5ea}
.nl-form{left:398px;top:1089px;width:197px;height:22px;background:#fff;border-radius:11px;display:flex;align-items:center;justify-content:space-between;padding-left:10px}
.nl-form span{font:400 7px/1 "Lato",sans-serif;color:#999}
.nl-form b{background:var(--brown-btn);color:#fff;font:700 6.5px/22px "Lato",sans-serif;padding:0 13px;border-radius:11px;height:22px}

/* footer */
.footer-social{left:186px;top:1158px}
.footer-logo{left:334px;top:1152px;font-size:23px}
.footer-links{left:462px;top:1152px;font:400 6.5px/1 "Lato",sans-serif;color:#888;display:flex;gap:11px}
.copyright{left:480px;top:1163px;font:400 6.5px/1 "Lato",sans-serif;color:#333}
.copyright em{font-style:normal;color:var(--green)}
</style>
</head>
<body>

<section class="abs hero"></section>
<div class="abs logo"><span class="dot"></span>tovira</div>
<nav class="abs nav"><span class="active">HOME</span><span>ABOUT</span><span>GO NATURAL</span><span>SHOP</span><span>CONTACT US</span></nav>
<div class="abs social header-social"><span></span><span></span><span></span><span></span><span></span></div>
<svg class="abs cart" width="12" height="12" viewBox="0 0 12 12"><path d="M1 3h2l1.5 5h5l1.2-3.5H4" fill="none" stroke="#555" stroke-width="1"/><circle cx="5" cy="10" r=".9" fill="#555"/><circle cx="9" cy="10" r=".9" fill="#555"/><circle cx="10" cy="3" r="2.4" fill="var(--green)"/></svg>

<div class="abs hero-photo" role="img" aria-label="Smiling woman with curly hair, bare shoulders"></div>
<div class="abs hero-bottles" role="img" aria-label="Three green bottles of the skin care range"></div>
<h1 class="abs hero-title">RULE YOUR SKIN</h1>
<p class="abs hero-sub">in 3 easy steps</p>
<ul class="abs steps">
  <li><svg width="14" height="8" viewBox="0 0 14 8"><path d="M1 6c2-3 5-3 6 0C5 7 3 7 1 6z" fill="var(--green)"/><path d="M7 5c1-3 4-5 6-4-1 3-3 5-6 4z" fill="var(--green)"/></svg>Refresh and Clean</li>
  <li><svg width="14" height="8" viewBox="0 0 14 8"><path d="M1 6c2-3 5-3 6 0C5 7 3 7 1 6z" fill="var(--green)"/><path d="M7 5c1-3 4-5 6-4-1 3-3 5-6 4z" fill="var(--green)"/></svg>Moisturize and Replenish</li>
  <li><svg width="14" height="8" viewBox="0 0 14 8"><path d="M1 6c2-3 5-3 6 0C5 7 3 7 1 6z" fill="var(--green)"/><path d="M7 5c1-3 4-5 6-4-1 3-3 5-6 4z" fill="var(--green)"/></svg>Hydrate and Soothe</li>
</ul>
<div class="abs badges"><span class="badge"><i></i></span><span class="badge"><i></i></span><span class="badge"><i></i></span></div>

<a class="abs tile tile-a" role="img" aria-label="Woman in white dress with arms open in a grassy field"><h2>RULE YOUR SKIN</h2><span class="btn-green">READ MORE</span></a>
<a class="abs tile tile-b" role="img" aria-label="Misty green tea plantation hills"><h2>AMAZING PRODUCTS</h2><span class="btn-green">READ MORE</span></a>

<h2 class="abs section-title">FEATURED PRODUCTS</h2>
<article class="abs product" style="left:79px"><div class="shot" role="img" aria-label="Green bottle of purifying tonic lotion"></div><h3>Purifying Tonic Lotion</h3><div class="stars">★★★★★</div><div class="price">$12.99</div><div class="btn-outline">ADD TO CART</div></article>
<article class="abs product" style="left:222px"><div class="shot" style="width:54px" role="img" aria-label="Green bottle of body lotion"></div><h3>Body Lotion</h3><div class="stars">★★★★★</div><div class="price">$15.99</div><div class="btn-outline">ADD TO CART</div></article>
<article class="abs product" style="left:365px"><div class="shot" style="width:30px" role="img" aria-label="Green spray bottle of facial cream"></div><h3>Facial Cream</h3><div class="stars">★★★★★</div><div class="price">$19.99</div><div class="btn-outline">ADD TO CART</div></article>
<article class="abs product" style="left:508px"><div class="shot" style="width:116px" role="img" aria-label="Three green bottles of the product bundle"></div><h3>Tovira Bundle</h3><div class="stars">★★★★★</div><div class="price">$45.00</div><div class="btn-outline">ADD TO CART</div></article>

<section class="abs testimonial"></section>
<h2 class="abs t-heading">WHAT OUR<br>HAPPY CLIENT SAY</h2>
<div class="abs t-rule"></div>
<div class="abs t-photo" role="img" aria-label="Portrait photo of a happy client"></div>
<span class="abs t-quote">“</span>
<p class="abs t-text">It is a long established fact that a reader will be distracted by the readable content of a more-or-less normal distribution of letters, as opposed to using 'Content here, content here', making it look like readable English. Many desktop publishing packages and web sites still in their infancy. <b style="color:var(--green);font:700 13px/1 'Playfair Display',serif">”</b></p>
<p class="abs t-name">- MARA DELCOURT</p>
<div class="abs dots"><span></span><span></span><span></span><span></span><span></span><span class="on"></span><span></span><span></span><span></span></div>

<div class="abs press"><span>Larkwell</span><span>PAVONA</span><span>Coral Ledger</span><span class="box"></span><span>driftline</span><span>HALBERD</span><span>Mirelune</span></div>

<section class="abs newsletter"></section>
<svg class="abs nl-icon" width="24" height="24" viewBox="0 0 24 24" fill="none" stroke="#fff" stroke-width="1.2"><rect x="2" y="9" width="20" height="13"/><path d="M2 9l10 8 10-8M6 12V3h12v9M9 6h6M9 9h6"/></svg>
<h3 class="abs nl-title">SIGN UP FOR OUR NEWSLETTER NOW</h3>
<p class="abs nl-sub">To stay in touch on our latest updates</p>
<form class="abs nl-form"><span>Email Address</span><b>SUBSCRIBE</b></form>

<div class="abs social footer-social"><span></span><span></span><span></span><span></span><span></span></div>
<div class="abs logo footer-logo"><span class="dot"></span>tovira</div>
<div class="abs footer-links"><span>Shipping</span><span>Privacy</span><span>Terms &amp; Conditions</span></div>
<p class="abs copyright">©2017 <em>Tovira</em> All rights reserved</p>

</body>
</html>
```